Korelith InsurTech Website Redesign - 10 Pages

Design a modern, professional website for Korelith, an AI-native cyber insurance platform serving SMBs.

DELIVERABLE: 10 pages (desktop + mobile mockups)
- Homepage (priority #1)
- 4 Platform pages (Cyber Insurance, Brokers, Underwriters, Policyholder)
- 3 Company pages (About Us, Team, Contact/Careers)
- 2 Risk pages (AI Risk, Cyber Risk)

DESIGN DIRECTION:
- Professional + innovative (insurance meets technology)
- Trust-building + modern aesthetic
- Reference: Brambury Insurance, Tidewick Insurance
- Use official brand colors (6-color palette provided)
- Avoid generic security clipart (padlocks, shields, magnifying glasses)
- Custom graphics, not AI-generated or stock imagery

CURRENT SITES FOR REFERENCE:
- www.korelith.ai
- https://a3c9124d.korelith-website.vorlapages.dev/

Full detailed brief with all content, page specifications, and brand guidelines attached as PDF (Korelith_PixelHarbor_Brief.pdf).

TARGET AUDIENCE: Insurance brokers (primary), SMB business owners (secondary)
KEY MESSAGE: "Cyber Insurance the Way It Should Be"

Additional brand assets available in Google Drive - link provided on request.

```html
<!DOCTYPE html>
<html lang="en">
<head>
<meta charset="utf-8">
<title>Korelith — Cyber Insurance the Way It Should Be</title>
<link rel="stylesheet" href="https://fonts.googleapis.com/css2?family=Montserrat:wght@500;600;700;800&family=Inter:wght@400;500;600&display=swap">
<style>
:root{
  --forest:#17403a;
  --forest-deep:#123531;
  --mint:#9cf29c;
  --mint-soft:#a6f3a6;
  --ink:#0e1e1b;
  --text:#3b4744;
  --muted:#5f6b68;
  --card:#f3f5f6;
  --teal-chip:#8fd9d0;
  --white:#ffffff;
}
*{box-sizing:border-box;margin:0;padding:0}
html,body{width:1200px;height:3535px;overflow:hidden}
body{position:relative;background:var(--white);font-family:"Inter",sans-serif;color:var(--ink)}
.abs{position:absolute}
h1,h2,h3,.display{font-family:"Montserrat",sans-serif}
.accent{color:var(--mint)}

/* header */
.site-header{position:absolute;left:0;top:0;width:1200px;height:77px;background:var(--white);display:flex;align-items:center;padding:0 60px 0 68px}
.brand{display:flex;align-items:center;gap:10px;font-family:"Montserrat",sans-serif;font-weight:700;font-size:30px;color:var(--forest);letter-spacing:.5px}
.brand-mark{width:22px;height:22px;background:var(--forest)}
.nav{display:flex;gap:36px;margin-left:26px;font-size:14px;color:var(--ink)}
.nav span{display:flex;align-items:center;gap:6px}
.btn-dark{margin-left:auto;background:var(--forest);color:#fff;font-weight:600;font-size:14px;padding:11px 21px;border-radius:3px}

/* hero */
.hero{position:absolute;left:0;top:77px;width:1200px;height:618px;background:var(--forest)}
.badge{left:60px;top:133px;border:1px solid #3f6d63;border-radius:16px;padding:6px 13px;font-size:13px;color:var(--mint);display:flex;align-items:center;gap:8px;letter-spacing:.3px}
.badge::before{content:"";width:6px;height:6px;border-radius:50%;background:var(--mint)}
.hero h1{left:60px;top:172px;font-size:61px;line-height:62px;font-weight:700;color:#fff}
.hero p{left:60px;top:382px;width:520px;font-size:16px;line-height:27px;color:#d5e3df}
.btn-light{left:60px;top:483px;background:#fff;color:var(--ink);font-size:14px;padding:12px 26px;border-radius:2px}
.hero-visual{left:620px;top:120px;width:531px;height:416px;border:3px solid #b9c6c3;border-radius:4px;background:radial-gradient(circle at 55% 45%,#6ff7e0 0,#2a7fa0 12%,#0f2a55 38%,#060d24 75%)}

/* section heads */
.section-title{left:0;width:1200px;text-align:center;font-size:42px;font-weight:700;color:var(--ink)}
.section-sub{left:300px;width:600px;text-align:center;font-size:20px;line-height:28px;color:var(--muted)}

/* feature cards */
.feature{border-radius:6px;padding:22px 20px}
.feature.grey{background:var(--card)}
.feature.green{background:var(--mint)}
.feature h3{font-size:28px;line-height:34px;font-weight:600;color:var(--ink)}
.feature p{font-size:12.5px;line-height:22px;color:var(--text)}
.icon-tile{width:80px;height:80px;border-radius:6px;background:#e3f0ef;display:flex;align-items:center;justify-content:center}
.icon-chip{width:44px;height:44px;border-radius:6px;display:flex;align-items:center;justify-content:center;flex:none}
.btn-outline{display:inline-flex;align-items:center;gap:8px;font-size:13.5px;padding:7px 9px;border-radius:4px;background:#fff;border:1px solid #d6dcda;color:var(--ink)}
.btn-outline.strong{border:2px solid var(--forest);color:var(--forest)}

/* lifecycle */
.stage{text-align:center;padding:0 8px}
.stage.panel{background:var(--mint);border-radius:18px}
.stage-art{width:120px;height:110px;margin:0 auto;border-radius:50%;background:radial-gradient(circle,#5fa86e 0,#c9f3cf 55%,rgba(255,255,255,0) 72%)}
.stage h3{font-size:20px;font-weight:700;color:var(--forest);margin-top:14px}
.stage p{font-size:14px;line-height:16.5px;color:#5f7a73;margin-top:8px}
.dots{display:flex;justify-content:center;gap:7px;margin-top:12px}
.dots i{width:6px;height:6px;border-radius:50%;border:1px solid var(--ink)}
.dots i.on{background:var(--ink)}

/* integrations */
.integrate h2{font-size:40px;line-height:48px;font-weight:700}
.node h4{font-family:"Montserrat",sans-serif;font-size:22px;line-height:27px;font-weight:600;color:var(--ink)}
.node p{font-size:13px;line-height:20px;color:var(--text);margin-top:8px}
.node-num{font-family:"Montserrat",sans-serif;font-weight:800;font-size:96px;color:#cfd3d2;line-height:1}

/* footer */
.site-footer{position:absolute;left:0;top:3011px;width:1200px;height:524px;background:var(--forest);color:#e4ece9}
.footer-brand{font-family:"Montserrat",sans-serif;font-weight:700;font-size:36px;color:var(--mint);letter-spacing:1px}
.footer-col h5{font-family:"Inter",sans-serif;font-weight:500;font-size:19px;letter-spacing:1.5px;color:#fff}
.footer-col a{display:block;font-size:13px;color:#d7e2de;text-decoration:none;margin-top:16px}
.social{display:flex;gap:14px}
.social i{width:15px;height:15px;border-radius:50%;background:#fff}
.legal{font-size:11.5px;color:#d7e2de}
.legal a{color:#d7e2de;margin-left:42px}
</style>
</head>
<body>

<header class="site-header">
  <div class="brand"><span class="brand-mark"></span>korelith</div>
  <nav class="nav">
    <span>Platform <svg width="12" height="8" viewBox="0 0 12 8"><path d="M1 1l5 5 5-5" fill="none" stroke="#0e1e1b" stroke-width="2"/></svg></span>
    <span>Cyber Risk</span>
    <span>AI Risk</span>
    <span>Company <svg width="12" height="8" viewBox="0 0 12 8"><path d="M1 1l5 5 5-5" fill="none" stroke="#0e1e1b" stroke-width="2"/></svg></span>
  </nav>
  <span class="btn-dark">Contact Us</span>
</header>

<section class="hero">
  <div class="abs badge">AI-NATIVE INTELLIGENCE</div>
  <h1 class="abs">Cyber Insurance<br>the Way It<br><span class="accent">Should Be.</span></h1>
  <p class="abs">Evidence based, automation driven underwriting for the AI era. We turn complex data into actionable protection.</p>
  <span class="abs btn-light">Contact Us</span>
  <div class="abs hero-visual" role="img" aria-label="Glowing network illustration linking identity platforms, developer platforms, endpoint security and cloud infrastructure into unified risk intelligence"></div>
</section>

<!-- What makes different -->
<h2 class="abs section-title" style="top:767px">What Makes <span class="accent">Korelith Different</span></h2>
<p class="abs section-sub" style="top:821px">Bridging the gap between deep insurance knowledge and cutting-edge technology.</p>

<div class="abs feature grey" style="left:60px;top:917px;width:510px;height:476px">
  <div class="icon-tile"><svg width="22" height="22" viewBox="0 0 22 22" fill="none" stroke="#17403a" stroke-width="1.6"><circle cx="11" cy="11" r="3"/><circle cx="4" cy="4" r="2"/><circle cx="18" cy="4" r="2"/><circle cx="4" cy="18" r="2"/><circle cx="18" cy="18" r="2"/><path d="M5.5 5.5L9 9M16.5 5.5L13 9M5.5 16.5L9 13M16.5 16.5L13 13"/></svg></div>
  <h3 style="margin-top:académ;margin-top:70px">End to End Cyber Risk and Insurance Platform</h3>
  <p style="margin-top:26px">The Korelith platform streamlines the entire policy lifecycle, incentivizes and empowers policyholders to actively reduce their risk, and elevates brokers as trusted advisors.</p>
  <span class="abs btn-outline strong" style="left:18px;top:420px">View Details <svg width="14" height="10" viewBox="0 0 14 10"><path d="M0 5h12M8 1l4 4-4 4" fill="none" stroke="#17403a" stroke-width="1.6"/></svg></span>
</div>

<div class="abs feature green" style="left:587px;top:917px;width:554px;height:229px">
  <div style="display:flex;gap:18px;align-items:flex-start">
    <div class="icon-chip" style="background:#eaf9ea"><svg width="16" height="16" viewBox="0 0 16 16" fill="none" stroke="#17403a" stroke-width="1.4"><rect x="2" y="2" width="12" height="12" rx="1"/><path d="M5 11V8M8 11V5M11 11V9"/></svg></div>
    <h3>Proprietary Tools and Rapid Response</h3>
  </div>
  <p style="margin-top:16px">Advanced security tools and 24/7 incident response capabilities protect businesses before, during, and after cyber events.</p>
  <span class="btn-outline" style="margin-top:16px">View Details <svg width="14" height="10" viewBox="0 0 14 10"><path d="M0 5h12M8 1l4 4-4 4" fill="none" stroke="#0e1e1b" stroke-width="1.6"/></svg></span>
</div>

<div class="abs feature grey" style="left:587px;top:1163px;width:554px;height:230px">
  <div style="display:flex;gap:18px;align-items:flex-start">
    <div class="icon-chip" style="background:var(--teal-chip);font-size:20px;color:#17403a">dna</div>
    <h3>Insurance DNA and Tech Execution</h3>
  </div>
  <p style="margin-top:14px">Founded by a team with deep expertise in cyber insurance and cybersecurity, we understand both the risk landscape and<br>the insurance market.</p>
  <span class="btn-outline" style="margin-top:12px">View Details <svg width="14" height="10" viewBox="0 0 14 10"><path d="M0 5h12M8 1l4 4-4 4" fill="none" stroke="#0e1e1b" stroke-width="1.6"/></svg></span>
</div>

<!-- Lifecycle -->
<h2 class="abs section-title" style="top:1563px">The Complete <span class="accent">Cyber Insurance Lifecycle</span></h2>
<p class="abs section-sub" style="top:1630px;left:200px;width:800px">A continuous flow of intelligence to keep your business resilient.</p>

<svg class="abs" style="left:0;top:0" width="1200" height="2300" viewBox="0 0 1200 2300">
  <path d="M110,1948 V1793 Q110,1773 130,1773 H281 Q301,1773 301,1793 V2153 Q301,2173 321,2173 H476 Q496,2173 496,2153 V1725 Q496,1705 516,1705 H675 Q695,1705 695,1725 V2153 Q695,2173 715,2173 H875 Q895,2173 895,2153 V1793 Q895,1773 915,1773 H1071 Q1091,1773 1091,1793 V1948" fill="none" stroke="#0e1e1b" stroke-width="3"/>
  <path d="M110,1942 l5,6 -5,6 -5,-6z M1091,1942 l5,6 -5,6 -5,-6z" fill="#0e1e1b"/>
</svg>

<div class="abs stage panel" style="left:124px;top:1789px;width:162px;height:326px;padding-top:28px">
  <div class="stage-art" role="img" aria-label="Shield with tick surrounded by policy documents"></div>
  <h3 style="margin-top:30px">ENSURE</h3>
  <p>Best in class cyber insurance coverage with comprehensive first and third party protections</p>
  <div class="dots"><i class="on"></i><i></i><i></i><i></i><i></i></div>
</div>

<div class="abs stage" style="left:310px;top:1840px;width:178px">
  <div class="stage-art" role="img" aria-label="Magnifying glass over charts with an API tag"></div>
  <h3 style="margin-top:24px">ASSESS</h3>
  <p>Dynamic scanning and read-only<br>API integrations to continuously evaluate risk posture and inform underwriting</p>
  <div class="dots"><i></i><i class="on"></i><i></i><i></i><i></i></div>
</div>

<div class="abs stage panel" style="left:514px;top:1720px;width:163px;height:323px;padding-top:20px">
  <div class="stage-art" role="img" aria-label="Rising bar chart with shield and trophy"></div>
  <h3 style="margin-top:16px">IMPROVE</h3>
  <p>Incentivize and guide policyholders to actively strengthen their cybersecurity through behavior rewards</p>
  <div class="dots"><i></i><i></i><i class="on"></i><i></i><i></i></div>
</div>

<div class="abs stage" style="left:702px;top:1852px;width:186px">
  <div class="stage-art" role="img" aria-label="Response toolkit with charts and investigation lens"></div>
  <h3 style="margin-top:24px">REMEDIATE</h3>
  <p>Expert post-breach services including forensics, restoration,<br>and crisis management support</p>
  <div class="dots"><i></i><i></i><i></i><i class="on"></i><i></i></div>
</div>

<div class="abs stage panel" style="left:912px;top:1789px;width:163px;height:326px;padding-top:28px">
  <div class="stage-art" role="img" aria-label="Renewal cycle around a shield with calendar"></div>
  <h3 style="margin-top:30px">RENEW</h3>
  <p>Seamless policy renewals with transparent pricing based on demonstrated risk improvements</p>
  <div class="dots"><i></i><i></i><i></i><i></i><i class="on"></i></div>
</div>

<!-- Integrations -->
<div class="abs integrate" style="left:60px;top:2350px;width:470px">
  <h2>Seamlessly<br>Integrates With <span class="accent">Your<br>Tech Stack</span></h2>
  <p style="margin-top:30px;font-size:13px;line-height:20px;color:var(--text)">We connect directly with the tools you already use to provide real-time risk visibility without the manual paperwork.</p>
  <span class="btn-outline strong" style="margin-top:48px">View Details <svg width="14" height="10" viewBox="0 0 14 10"><path d="M0 5h12M8 1l4 4-4 4" fill="none" stroke="#17403a" stroke-width="1.6"/></svg></span>
</div>

<svg class="abs" style="left:540px;top:2330px" width="620" height="620" viewBox="540 2330 620 620">
  <g stroke="#9cf29c" stroke-width="3" stroke-dasharray="4 6" fill="none">
    <line x1="847" y1="2668" x2="780" y2="2470"/>
    <line x1="847" y1="2668" x2="1000" y2="2585"/>
    <line x1="847" y1="2668" x2="690" y2="2730"/>
    <line x1="847" y1="2668" x2="940" y2="2810"/>
  </g>
  <circle cx="847" cy="2668" r="164" fill="none" stroke="#9cf29c" stroke-width="4"/>
  <circle cx="847" cy="2668" r="72" fill="#17403a"/>
  <text x="847" y="2660" text-anchor="middle" font-family="Montserrat,sans-serif" font-weight="700" font-size="19" fill="#fff">UNIFIED</text>
  <text x="847" y="2684" text-anchor="middle" font-family="Inter,sans-serif" font-size="13" fill="#cfe0db">Risk Intelligence</text>
  <!-- cloud icon -->
  <g fill="none" stroke="#8fd9d0" stroke-width="1.6">
    <path d="M730 2370a9 9 0 0 1 17-4 7 7 0 0 1 4 13h-21a5 5 0 0 1 0-9z"/>
    <rect x="718" y="2388" width="10" height="6"/><rect x="736" y="2388" width="10" height="6"/><rect x="754" y="2388" width="10" height="6"/>
    <!-- shield -->
    <path d="M1046 2466l20 7v14c0 12-9 19-20 23-11-4-20-11-20-23v-14z"/><path d="M1037 2487l6 6 12-12"/>
    <!-- id card -->
    <rect x="568" y="2666" width="46" height="30" rx="2"/><circle cx="582" cy="2679" r="5"/><path d="M574 2691a8 8 0 0 1 16 0M596 2676h12M596 2683h12M585 2656v10"/>
    <!-- code -->
    <path d="M961 2812l-8 8 8 8M989 2812l8 8-8 8M979 2808l-8 24"/>
  </g>
</svg>

<div class="abs node" style="left:666px;top:2405px"><span class="abs node-num" style="left:0;top:0">4</span></div>
<div class="abs node" style="left:715px;top:2408px;width:170px"><h4>Cloud Infrastructure</h4><p>Examples: Stratocloud, Nimbra, Orbitcloud</p></div>

<div class="abs node" style="left:983px;top:2515px"><span class="node-num">3</span></div>
<div class="abs node" style="left:1020px;top:2532px;width:140px"><h4>Endpoint Security</h4><p>Examples:<br>Sentrywave,<br>Bastionguard,<br>Helixwatch XDR</p></div>

<div class="abs node" style="left:524px;top:2702px"><span class="node-num">1</span></div>
<div class="abs node" style="left:564px;top:2714px;width:150px"><h4>Identity Platforms</h4><p>Examples: Officelane Suite, Keyloom, Nimbra Directory</p></div>

<div class="abs node" style="left:905px;top:2840px"><span class="node-num">2</span></div>
<div class="abs node" style="left:947px;top:2855px;width:200px"><h4>Developer Platforms</h4><p>Examples: Codeharbor, Repotrail</p></div>

<!-- Footer -->
<footer class="site-footer">
  <div class="abs footer-brand" style="left:91px;top:88px">korelith</div>
  <p class="abs" style="left:91px;top:155px;width:310px;font-size:12.5px;line-height:22px;color:#d7e2de">The intelligence-first approach to cyber insurance. Built for the modern enterprise, powered by automation.</p>
  <p class="abs" style="left:91px;top:235px;font-size:12.5px;color:#9fb7b0">Office Location:</p>
  <p class="abs" style="left:91px;top:258px;font-size:12.5px;color:#fff">Marlow Springs, UNITED STATES</p>
  <p class="abs" style="left:91px;top:289px;font-size:12.5px;color:#fff">+1 555 014 2210</p>
  <p class="abs" style="left:91px;top:314px;font-size:12.5px;color:#fff">contact@korelith.com</p>
  <div class="abs social" style="left:92px;top:354px"><i></i><i></i><i></i><i></i><i></i></div>

  <div class="abs footer-col" style="left:515px;top:84px"><h5>PLATFORM</h5><a>Insurance</a><a>Brokers</a><a>Underwriters</a><a>Risk Portal</a></div>
  <div class="abs footer-col" style="left:725px;top:84px"><h5>SOLUTIONS</h5><a>Cyber Risk</a><a>AI Risk</a><a>Integrations</a><a>Security Ops</a></div>
  <div class="abs footer-col" style="left:935px;top:84px"><h5>COMPANY</h5><a>About Us</a><a>Team</a><a>Careers</a><a>Contact</a></div>

  <div class="abs" style="left:66px;top:414px;width:1068px;height:1px;background:#2f5a52"></div>
  <div class="abs legal" style="left:67px;top:450px">© 2026 Korelith Inc. All rights reserved.</div>
  <div class="abs legal" style="right:77px;top:450px"><a>Privacy Policy</a><a>Terms of Service</a><a>Cookie Settings</a></div>
</footer>

</body>
</html>
```